We need a new brochure design for our dental clinic, Birchfield Dental. We have attached the information we want printed and photos to include.

Industry/Entity Type

Dental

```html
<!DOCTYPE html>
<html lang="en">
<head>
<meta charset="utf-8">
<title>Birchfield Dental Brochure</title>
<link href="https://fonts.googleapis.com/css2?family=Didact+Gothic&display=swap" rel="stylesheet">
<style>
  :root {
    --blue-deep: #0a63b8;
    --blue-mid: #1e86d6;
    --blue-light: #3fa9ec;
    --green: #7ac142;
    --green-light: #b5dc4a;
    --ink: #232323;
    --white: #ffffff;
  }
  html, body { margin: 0; padding: 0; overflow: hidden; background: #ffffff; }
  .brochure {
    position: relative;
    width: 1200px; height: 848px;
    overflow: hidden;
    background: var(--white);
    font-family: "Didact Gothic", "Helvetica Neue", Arial, sans-serif;
  }
  .backdrop { position: absolute; inset: 0; }
  .bio {
    position: absolute; left: 14px; top: 14px; width: 380px;
    font-size: 12.6px; line-height: 1.22; color: var(--ink); margin: 0;
    letter-spacing: 0.2px;
  }
  .bio p { margin: 0 0 15px; }
  .doctor-photo {
    position: absolute; left: 40px; top: 380px; width: 320px; height: 468px;
    border-radius: 150px 150px 0 0;
    background: linear-gradient(180deg, #2a3a4e 0%, #2f6fa9 45%, #1c4f86 100%);
    opacity: 0.85;
  }
  .services-title {
    position: absolute; right: 810px; top: 370px;
    color: var(--white); font-size: 29px; line-height: 1.12; text-align: right;
    margin: 0; font-weight: 400; letter-spacing: 0.5px;
  }
  .services-list {
    position: absolute; left: 416px; top: 374px; margin: 0; padding: 0; list-style: none;
    color: var(--white); font-size: 25.5px; line-height: 29px; letter-spacing: 0.6px;
  }
  .instalment {
    position: absolute; left: 416px; top: 764px; margin: 0;
    color: var(--green); font-size: 25px; line-height: 32px; letter-spacing: 0.8px;
  }
  .clinic-photo {
    position: absolute; left: 400px; top: 48px; width: 184px; height: 184px;
    border-radius: 50%; border: 10px solid var(--blue-mid); box-sizing: border-box;
    background: radial-gradient(circle at 50% 45%, #f4f8fb 0%, #dbe6ee 55%, #b9cbd8 100%);
    box-shadow: 0 0 0 3px #cfe4f6;
  }
  .relax-note {
    position: absolute; right: 422px; top: 244px; margin: 0; text-align: right;
    color: var(--ink); font-size: 16px; line-height: 20px; letter-spacing: 0.3px;
  }
  .smile-photo {
    position: absolute; left: 930px; top: 0; width: 270px; height: 250px;
    border-radius: 0 0 0 160px;
    background: radial-gradient(ellipse at 55% 40%, #ffffff 0%, #f5d6dd 40%, #e07a9a 70%, #fbeef1 100%);
  }
  .headline {
    position: absolute; left: 802px; width: 398px; top: 278px; margin: 0;
    text-align: center; color: var(--green); font-size: 35px; line-height: 44px;
    font-weight: 400; letter-spacing: 1px;
  }
  .brand {
    position: absolute; left: 862px; top: 490px; display: flex; align-items: center; gap: 24px;
  }
  .brand-mark {
    width: 64px; height: 64px; background: var(--white); border-radius: 50%;
  }
  .brand-name {
    color: var(--white); font-size: 34px; line-height: 42px; text-align: center; margin: 0;
    letter-spacing: 0.5px;
  }
  .call-to-action {
    position: absolute; left: 802px; width: 398px; top: 622px; margin: 0;
    text-align: center; color: var(--white); font-size: 23px; line-height: 30px; letter-spacing: 0.4px;
  }
  .phone-box {
    position: absolute; left: 864px; top: 690px; width: 274px; height: 68px;
    background: var(--white); border-radius: 10px;
    display: flex; align-items: center; justify-content: center; gap: 12px;
    color: var(--blue-mid); font-size: 37px; letter-spacing: 1px;
  }
  .phone-box svg { width: 40px; height: 40px; }
  .email {
    position: absolute; left: 802px; width: 398px; top: 768px; margin: 0;
    text-align: center; color: var(--white); font-size: 25px; letter-spacing: 0.8px;
  }
</style>
</head>
<body>
<main class="brochure">
  <svg class="backdrop" width="1200" height="848" viewBox="0 0 1200 848" aria-hidden="true">
    <defs>
      <linearGradient id="blueFill" x1="0" y1="0" x2="0" y2="1">
        <stop offset="0" stop-color="#3fa9ec"/>
        <stop offset="0.5" stop-color="#1e86d6"/>
        <stop offset="1" stop-color="#0a63b8"/>
      </linearGradient>
      <linearGradient id="greenFade" x1="0" y1="0" x2="1" y2="0.6">
        <stop offset="0" stop-color="#7ac142"/>
        <stop offset="0.55" stop-color="#b5dc4a" stop-opacity="0.5"/>
        <stop offset="1" stop-color="#ffffff" stop-opacity="0"/>
      </linearGradient>
      <linearGradient id="greenBand" x1="0" y1="0" x2="1" y2="0">
        <stop offset="0" stop-color="#7ac142"/>
        <stop offset="1" stop-color="#b5dc4a"/>
      </linearGradient>
    </defs>
    <rect x="0" y="0" width="402" height="340" fill="url(#greenFade)"/>
    <path d="M0,300 C150,250 300,300 402,330 C560,370 700,330 802,300 L802,360 L0,360 Z" fill="url(#greenBand)"/>
    <path d="M0,352 C150,320 300,350 402,362 C560,385 700,360 802,338 L802,848 L0,848 Z" fill="url(#blueFill)"/>
    <path d="M802,390 C900,430 1050,420 1200,350 L1200,400 C1060,440 920,450 802,430 Z" fill="url(#greenBand)"/>
    <path d="M802,420 C920,445 1060,435 1200,392 L1200,848 L802,848 Z" fill="url(#blueFill)"/>
    <line x1="402" y1="0" x2="402" y2="848" stroke="#ffffff" stroke-width="2"/>
    <line x1="802" y1="0" x2="802" y2="848" stroke="#ffffff" stroke-width="2"/>
  </svg>

  <section class="bio">
    <p>Dr Arvind K. Rahman obtained his BDS from Eastbay University. Upon graduation he served in various government institutions such as The Central Dental Institute, Wellness Outreach Council, National Defence Corps and Harbourcare Polyclinics.</p>
    <p>In 2009 Dr Arvind left the government sector for private practice. As a firm believer of continual education he is an alumni member of the Westgate Institute of Advanced Dental Studies. At the institute he received training from renowned dentists Dr Mark Ellison and Dr Lena Hart in the subjects of aesthetic restorative dentistry and root canal treatment.</p>
    <p>In 2014 Dr Arvind was admitted as a fellow at the prestigious Pacific College of Dental Surgeons. Dr Arvind has also completed his part 1 exams for the Diploma of Membership of the Joint Dental Faculties at the Academy of Dental Surgeons (MDF ADS).</p>
  </section>

  <div class="doctor-photo" role="img" aria-label="Portrait photo of the dentist in scrubs with dental loupes"></div>

  <h2 class="services-title">SERVICE<br>PROVIDED</h2>
  <ul class="services-list">
    <li>Dental Implants</li>
    <li>Clear Aligners</li>
    <li>Smile makeovers</li>
    <li>Dental Orthopaedic Treatment</li>
    <li>Braces for Children &amp; Adults</li>
    <li>Dental fillings &amp;</li>
    <li>Porcelain restorations</li>
    <li>Gum Treatments</li>
    <li>Root canal Treatments</li>
    <li>Wisdom tooth surgery</li>
    <li>Dentures</li>
    <li>Children's dentistry</li>
    <li>Digital X-rays</li>
  </ul>
  <p class="instalment">0% interest free<br>instalment plans available.</p>

  <div class="clinic-photo" role="img" aria-label="Photo of the bright clinic reception and entrance"></div>
  <p class="relax-note">Feel free to relax<br>and ask our friendly<br>staff for some light refreshments before<br>or after your dental treatment</p>

  <div class="smile-photo" role="img" aria-label="Close-up photo of a bright healthy smile"></div>
  <h1 class="headline">A Healthier Smile For<br>A Healthier You</h1>

  <div class="brand">
    <div class="brand-mark"></div>
    <p class="brand-name">Birchfield<br>Dental</p>
  </div>

  <p class="call-to-action">Call us for an<br>appointment today.</p>
  <div class="phone-box">
    <svg viewBox="0 0 24 24" aria-hidden="true"><path fill="#1e86d6" d="M6.6 10.8c1.4 2.8 3.8 5.1 6.6 6.6l2.2-2.2c.3-.3.7-.4 1-.2 1.1.4 2.300.6 3.6.6.6 0 1 .4 1 1V20c0 .6-.4 1-1 1C10.6 21 3 13.4 3 4c0-.6.4-1 1-1h3.5c.6 0 1 .4 1 1 0 1.3.2 2.5.6 3.6.1.3 0 .7-.2 1L6.6 10.8z"/></svg>
    <span>6123 4870</span>
  </div>
  <p class="email">info@birchfielddental.com.sg</p>
</main>
</body>
</html>
```